Flyer for a Payroll and Bookkeeping Companmy

Need a brochure to highlight our costs and service to hand out to clients.

Please see attachments for more information.

Industry/Entity Type

It Service

```html
<!DOCTYPE html>
<html lang="en">
<head>
<meta charset="utf-8">
<title>Harbor Summit – Bookkeeping Pricing</title>
<link rel="stylesheet" href="https://fonts.googleapis.com/css2?family=Open+Sans:wght@400;600;700&display=swap">
<style>
  :root {
    --page-bg: #ffffff;
    --edge-red: #d9534f;
    --frame: #222222;
    --title-orange: #ef7d22;
    --brand-blue: #1f6fb5;
    --services-grey: #7f8c8d;
    --premium-top: #c91f78;
    --premium-price: #9c2280;
    --entre-top: #f6b219;
    --entre-price: #ee8a23;
    --growth-top: #93c83f;
    --growth-price: #7f9a3a;
    --setup-top: #1ab3d3;
    --setup-price: #1c73ba;
    --row-alt: #efefef;
    --row-plain: #ffffff;
    --cell-line: #d6d6d6;
    --text-dark: #1d1d1d;
    --tick-green: #8cc63f;
    --cross-red: #e2231a;
  }
  * { box-sizing: border-box; margin: 0; padding: 0; }
  html, body {
    width: 1200px; height: 943px; overflow: hidden;
    background: var(--page-bg);
    font-family: "Open Sans", Arial, sans-serif;
    color: var(--text-dark);
  }
  .canvas {
    position: relative; width: 1200px; height: 943px;
    border: 1px solid var(--edge-red);
  }
  .frame {
    position: absolute; left: 34px; top: 35px; width: 1131px; height: 875px;
    border: 1px solid var(--frame);
  }
  .brand {
    position: absolute; left: 94px; top: 142px;
    display: flex; align-items: center; gap: 10px;
  }
  .brand-dot { width: 30px; height: 30px; border-radius: 50%; background: var(--brand-blue); }
  .brand-name {
    font-weight: 700; font-size: 24px; color: var(--brand-blue); letter-spacing: -0.3px;
  }
  .title {
    position: absolute; left: 360px; top: 100px; width: 640px; text-align: center;
    font-weight: 600; font-size: 60px; line-height: 1; color: var(--title-orange);
    letter-spacing: -0.3px;
  }
  .pricing {
    position: absolute; left: 92px; top: 225px; width: 1011px;
    display: grid;
    grid-template-columns: 271px repeat(4, 185px);
    grid-template-rows: 53px 68px repeat(8, 62px);
    background: var(--row-plain);
    box-shadow: 0 0 0 8px #e4e4e4, 6px 8px 12px 8px rgba(0,0,0,0.25);
  }
  .services-head {
    grid-row: 1 / 3; grid-column: 1;
    background: var(--services-grey); color: #fff;
    display: flex; align-items: center; justify-content: center;
    font-weight: 600; font-size: 32px;
  }
  .plan-name {
    display: flex; align-items: center; justify-content: center;
    color: #fff; font-weight: 700; font-size: 21px;
    border-left: 1px solid #fff;
  }
  .plan-price {
    position: relative;
    display: flex; align-items: center; justify-content: center;
    color: #fff; font-weight: 700; font-size: 37px;
    border-left: 1px solid #fff;
  }
  .plan-price::after {
    content: ""; position: absolute; left: 50%; bottom: -14px; margin-left: -18px;
    border-left: 18px solid transparent; border-right: 18px solid transparent;
    border-top: 14px solid var(--notch); z-index: 2;
  }
  .plan-name.premium { background: var(--premium-top); }
  .plan-price.premium { background: var(--premium-price); --notch: var(--premium-price); }
  .plan-name.entrepreneur { background: var(--entre-top); }
  .plan-price.entrepreneur { background: var(--entre-price); --notch: var(--entre-price); }
  .plan-name.growth { background: var(--growth-top); }
  .plan-price.growth { background: var(--growth-price); --notch: var(--growth-price); }
  .plan-name.setup { background: var(--setup-top); }
  .plan-price.setup { background: var(--setup-price); --notch: var(--setup-price); }

  .row-label, .cell {
    display: flex; flex-direction: column; justify-content: center;
    border-bottom: 1px solid var(--cell-line);
    font-size: 14px; line-height: 1.3;
  }
  .row-label {
    padding-left: 12px; font-weight: 600; font-size: 14px;
  }
  .row-label small { display: block; font-weight: 400; font-size: 13.5px; }
  .cell {
    align-items: center; text-align: center;
    border-left: 1px solid var(--cell-line);
  }
  .cell .note { font-weight: 600; font-size: 14px; margin-top: 2px; }
  .alt { background: var(--row-alt); }
  .icon { width: 26px; height: 26px; }
</style>
</head>
<body>
<svg width="0" height="0" style="position:absolute" aria-hidden="true">
  <defs>
    <symbol id="tick" viewBox="0 0 26 26">
      <circle cx="13" cy="13" r="11" fill="none" stroke="#8cc63f" stroke-width="2.4"/>
      <path d="M7.5 13.5 L11.5 17.2 L18.5 9" fill="none" stroke="#8cc63f" stroke-width="2.6" stroke-linecap="round" stroke-linejoin="round"/>
    </symbol>
    <symbol id="cross" viewBox="0 0 26 26">
      <path d="M5 5 L21 21 M21 5 L5 21" stroke="#e2231a" stroke-width="2.6" stroke-linecap="round"/>
    </symbol>
  </defs>
</svg>

<div class="canvas">
  <div class="frame"></div>

  <div class="brand">
    <span class="brand-dot"></span>
    <span class="brand-name">Harbor Summit</span>
  </div>

  <h1 class="title">Bookkeeping Pricing</h1>

  <div class="pricing">
    <div class="services-head">Services</div>
    <div class="plan-name premium">Premium</div>
    <div class="plan-name entrepreneur">Entrepreneur</div>
    <div class="plan-name growth">Growth</div>
    <div class="plan-name setup">Set Up</div>
    <div class="plan-price premium">$999</div>
    <div class="plan-price entrepreneur">$599</div>
    <div class="plan-price growth">$299</div>
    <div class="plan-price setup">$149</div>

    <div class="row-label alt">Employees</div>
    <div class="cell alt">Around<br>10+</div>
    <div class="cell alt">Around<br>5–9</div>
    <div class="cell alt">Around<br>2–5</div>
    <div class="cell alt">Around<br>1–2</div>

    <div class="row-label">Transactions / Month</div>
    <div class="cell">Up to<br>250</div>
    <div class="cell">Up to<br>150</div>
    <div class="cell">Up to<br>75</div>
    <div class="cell">Up to<br>50</div>

    <div class="row-label alt">Bookkeeping</div>
    <div class="cell alt"><svg class="icon"><use href="#tick"/></svg><span class="note">Weekly</span></div>
    <div class="cell alt"><svg class="icon"><use href="#tick"/></svg><span class="note">Weekly</span></div>
    <div class="cell alt"><svg class="icon"><use href="#tick"/></svg><span class="note">Monthly</span></div>
    <div class="cell alt"><svg class="icon"><use href="#tick"/></svg><span class="note">Quarterly</span></div>

    <div class="row-label">Financial Reports &amp; Review</div>
    <div class="cell"><svg class="icon"><use href="#tick"/></svg><span class="note">Weekly</span></div>
    <div class="cell"><svg class="icon"><use href="#tick"/></svg><span class="note">Monthly</span></div>
    <div class="cell"><svg class="icon"><use href="#tick"/></svg><span class="note">Monthly</span></div>
    <div class="cell"><svg class="icon"><use href="#tick"/></svg><span class="note">Quarterly</span></div>

    <div class="row-label alt">Support<small>(Phone and Chatterly)</small></div>
    <div class="cell alt"><svg class="icon"><use href="#tick"/></svg></div>
    <div class="cell alt"><svg class="icon"><use href="#tick"/></svg></div>
    <div class="cell alt"><svg class="icon"><use href="#tick"/></svg></div>
    <div class="cell alt"><svg class="icon"><use href="#tick"/></svg></div>

    <div class="row-label">Online Collaboration Portal<small>(CloudShelf)</small></div>
    <div class="cell"><svg class="icon"><use href="#tick"/></svg></div>
    <div class="cell"><svg class="icon"><use href="#tick"/></svg></div>
    <div class="cell"><svg class="icon"><use href="#tick"/></svg></div>
    <div class="cell"><svg class="icon"><use href="#tick"/></svg></div>

    <div class="row-label alt">Business Tax Return</div>
    <div class="cell alt"><svg class="icon"><use href="#tick"/></svg></div>
    <div class="cell alt"><svg class="icon"><use href="#tick"/></svg></div>
    <div class="cell alt">$799</div>
    <div class="cell alt">$599</div>

    <div class="row-label">Bill Pay<small>(with Approval Process)</small></div>
    <div class="cell"><svg class="icon"><use href="#tick"/></svg><span class="note">$5 / Payment</span></div>
    <div class="cell"><svg class="icon"><use href="#cross"/></svg></div>
    <div class="cell"><svg class="icon"><use href="#cross"/></svg></div>
    <div class="cell"><svg class="icon"><use href="#cross"/></svg></div>
  </div>
</div>
</body>
</html>
```